Independent manufacturing consultant needs a professional Logo & biz card Update

I want a new logo using the existing one as inspiration. The company legal name is Corvex Industrial Trade & Advisory Partners, Inc. Often the name is shortened to Corvex ITP and that matches with web address of www.corvex-itp.example. #1 create a new logo and #2 update biz card. I will need vector file to get cards printed (bilingual English & Japanese). The reverse side will be an exact copy of the original design but in Japanese. I have another resource for the translation so that is not in this scope.
Next month, a follow-up project will be to update the website using new logo and get a professional, cohesive look to all the pages.
Check out web site to get an idea of what we do. The desire is to project professional, articulate, clean, dependable, detailed oriented team of experts.

Target Market(s)

Food and Beverage manufactures. Major players, regiona, and start ups.

Industry/Entity Type

It Company

Contact Information for Business Card

exisiting card and logo provided as foundation but ready to improve upon both!

Logo Text

Corvex ITP or other....

Font styles to use
Sans Serif

Colors
9bcb3c
0356a4

Requirements
Must have
• Logo and biz card.
• Logo will be used for other materials and website.
Nice to have
• open to suggestions.
• Like the Green & Blue colors but also dig grey scale as the website incorporates.
• Open to suggestions.
Should not have
• not to animated. I work with more conservative clients.

```html
<!DOCTYPE html>
<html lang="en">
<head>
<meta charset="utf-8">
<title>Corvex ITP — Business Card</title>
<link rel="stylesheet" href="https://fonts.googleapis.com/css2?family=Source+Sans+3:wght@400;600;700&family=Noto+Sans+JP:wght@400;700&display=swap">
<style>
  :root {
    --brand-green: #8cc63f;
    --brand-blue: #2a5aa6;
    --brand-blue-light: #0a90d8;
    --ink-grey: #6d6e71;
    --rule-grey: #c4c6c9;
    --card-white: #ffffff;
    --backdrop: #eef0f2;
  }
  * { box-sizing: border-box; margin: 0; padding: 0; }
  html, body {
    width: 1200px; height: 1000px; overflow: hidden;
    background: var(--backdrop);
    font-family: "Source Sans 3", "Noto Sans JP", sans-serif;
  }
  .sheet {
    position: relative; width: 1200px; height: 1000px;
    display: flex; flex-direction: column; align-items: center; justify-content: center; gap: 70px;
  }
  .card {
    position: relative; width: 620px; height: 354px;
    background: var(--card-white);
    box-shadow: 0 6px 22px rgba(0,0,0,0.12);
    overflow: hidden;
  }
  .card__band {
    position: absolute; left: 0; right: 0; bottom: 0; height: 20px;
    background: linear-gradient(90deg, var(--brand-blue) 0%, var(--brand-blue-light) 100%);
  }
  .card__divider { position: absolute; left: 0; top: 0; width: 620px; height: 354px; }
  .identity { position: absolute; left: 470px; top: 46px; }
  .identity__name {
    color: var(--brand-green); font-weight: 700; font-size: 25px; letter-spacing: 0.2px; line-height: 1;
  }
  .identity__title { color: var(--ink-grey); font-size: 18px; margin-top: 4px; }
  .identity__title--jp { font-family: "Noto Sans JP", sans-serif; font-size: 17px; }
  .contact { position: absolute; left: 446px; top: 190px; list-style: none; }
  .contact__item {
    display: flex; align-items: center; gap: 4px;
    color: var(--ink-grey); font-size: 16px; line-height: 27px;
  }
  .contact__icon { width: 14px; height: 14px; flex: none; }
  .brand { position: absolute; left: 54px; bottom: 52px; }
  .brand__name {
    color: var(--brand-blue); font-weight: 700; font-size: 58px; line-height: 1; letter-spacing: -0.5px;
  }
  .brand__tagline { color: var(--ink-grey); font-size: 19px; margin-top: 2px; }
  .brand__tagline--jp { font-family: "Noto Sans JP", sans-serif; font-size: 16px; margin-top: 6px; }
</style>
</head>
<body>
<main class="sheet">

  <!-- English side -->
  <article class="card" lang="en">
    <svg class="card__divider" viewBox="0 0 620 354" aria-hidden="true">
      <defs>
        <linearGradient id="rule-en" x1="0" y1="0" x2="0" y2="1">
          <stop offset="0" stop-color="#c4c6c9" stop-opacity="0.2"/>
          <stop offset="0.4" stop-color="#c4c6c9"/>
          <stop offset="1" stop-color="#c4c6c9" stop-opacity="0.3"/>
        </linearGradient>
      </defs>
      <line x1="374" y1="38" x2="432" y2="304" stroke="url(#rule-en)" stroke-width="2"/>
    </svg>
    <div class="identity">
      <p class="identity__name">DANA OSTRAND</p>
      <p class="identity__title">Principal</p>
    </div>
    <ul class="contact">
      <li class="contact__item">
        <svg class="contact__icon" viewBox="0 0 14 14" aria-hidden="true"><rect x="3" y="1" width="8" height="12" rx="1.5" fill="#0a90d8"/><rect x="4.5" y="3" width="5" height="6" fill="#fff"/></svg>
        <span>: 555.014.2290</span>
      </li>
      <li class="contact__item">
        <svg class="contact__icon" viewBox="0 0 14 14" aria-hidden="true"><rect x="1" y="3" width="12" height="8" fill="#0a90d8"/><path d="M1 3 L7 8 L13 3" fill="none" stroke="#fff" stroke-width="1.2"/></svg>
        <span>: dana@corvex-itp.example</span>
      </li>
      <li class="contact__item">
        <svg class="contact__icon" viewBox="0 0 14 14" aria-hidden="true"><rect x="1" y="2" width="12" height="10" rx="1" fill="#0a90d8"/><rect x="2.5" y="4.5" width="9" height="6" fill="#fff"/></svg>
        <span>: www.corvex-itp.example</span>
      </li>
    </ul>
    <div class="brand">
      <p class="brand__name">Corvex ITP</p>
      <p class="brand__tagline">Industrial Trade &amp; Advisory Partners</p>
    </div>
    <div class="card__band"></div>
  </article>

  <!-- Japanese side -->
  <article class="card" lang="ja">
    <svg class="card__divider" viewBox="0 0 620 354" aria-hidden="true">
      <defs>
        <linearGradient id="rule-jp" x1="0" y1="0" x2="0" y2="1">
          <stop offset="0" stop-color="#c4c6c9" stop-opacity="0.2"/>
          <stop offset="0.4" stop-color="#c4c6c9"/>
          <stop offset="1" stop-color="#c4c6c9" stop-opacity="0.3"/>
        </linearGradient>
      </defs>
      <line x1="374" y1="38" x2="432" y2="304" stroke="url(#rule-jp)" stroke-width="2"/>
    </svg>
    <div class="identity">
      <p class="identity__name" lang="en">DANA OSTRAND</p>
      <p class="identity__title identity__title--jp">主要な</p>
    </div>
    <ul class="contact" lang="en">
      <li class="contact__item">
        <svg class="contact__icon" viewBox="0 0 14 14" aria-hidden="true"><rect x="3" y="1" width="8" height="12" rx="1.5" fill="#0a90d8"/><rect x="4.5" y="3" width="5" height="6" fill="#fff"/></svg>
        <span>: 555.014.2290</span>
      </li>
      <li class="contact__item">
        <svg class="contact__icon" viewBox="0 0 14 14" aria-hidden="true"><rect x="1" y="3" width="12" height="8" fill="#0a90d8"/><path d="M1 3 L7 8 L13 3" fill="none" stroke="#fff" stroke-width="1.2"/></svg>
        <span>: dana@corvex-itp.example</span>
      </li>
      <li class="contact__item">
        <svg class="contact__icon" viewBox="0 0 14 14" aria-hidden="true"><rect x="1" y="2" width="12" height="10" rx="1" fill="#0a90d8"/><rect x="2.5" y="4.5" width="9" height="6" fill="#fff"/></svg>
        <span>: www.corvex-itp.example</span>
      </li>
    </ul>
    <div class="brand">
      <p class="brand__name" lang="en">Corvex ITP</p>
      <p class="brand__tagline brand__tagline--jp">インダストリアル・トレード&amp;アドバイザリー</p>
    </div>
    <div class="card__band"></div>
  </article>

</main>
</body>
</html>
```